Dunmore County Assessor Canditate

We need a billboard ad for a political candidate Rosa Terwilliger who is running for Dunmore County Assessor in an upcoming election. Needs to be simple and to the point to get the people to see the name "Rosa Terwilliger" and what to vote for "Dunmore County Assessor" in Las Vegas, NV. Also the billboard visibility is best in the top side of the sign, so the information should be most prominent in the top right, middle, left sides.The size of the billboard is 14 ft Height X 48 ft Wide Also needs some bright colors that are noticable from a freeway viewed billboard.Designers - I need to have "Paid for by Rosa Terwilliger for Dunmore County Assessor" on the sign
I have uploaded a few headshots you can work with to create a design. Thank you,

http://rosaterwilliger.info/

Target Market(s)

Voters

Industry/Entity Type

Political

Requirements
Must have
• Name, what I am voting for, and some image that represents Las Vegas and/or Nevada

```html
<!DOCTYPE html>
<html lang="en">
<head>
<meta charset="utf-8">
<title>Rosa Terwilliger for Dunmore County Assessor</title>
<link rel="stylesheet" href="https://fonts.googleapis.com/css2?family=Barlow+Semi+Condensed:wght@600;700;800&display=swap">
<style>
  :root {
    --ink: #222222;
    --yellow: #f7ef4a;
    --white: #ffffff;
    --muted: #bdbdbd;
    --page: #e9ecf2;
    --photo-light: #3a3633;
    --photo-dark: #141312;
  }
  * { margin: 0; padding: 0; box-sizing: border-box; }
  html, body { width: 1200px; height: 848px; overflow: hidden; background: var(--page); }
  .billboard {
    position: absolute;
    left: 20px; top: 255px;
    width: 1160px; height: 338px; /* 48 ft x 14 ft */
    background: var(--ink);
    overflow: hidden;
    font-family: "Barlow Semi Condensed", sans-serif;
  }
  .candidate-photo {
    position: absolute;
    left: 0; top: 0;
    width: 470px; height: 338px;
    background: radial-gradient(ellipse at 50% 40%, var(--photo-light) 0%, var(--photo-dark) 75%);
  }
  .bands {
    position: absolute;
    left: 0; top: 0;
    width: 100%; height: 100%;
  }
  .candidate-name {
    position: absolute;
    left: 450px; right: 16px; top: 16px;
    height: 112px;
    display: flex; align-items: center; justify-content: center;
    font-weight: 800;
    font-size: 78px;
    line-height: 1;
    color: var(--ink);
    white-space: nowrap;
  }
  .office {
    position: absolute;
    left: 520px; right: 30px; top: 138px;
    text-align: center;
  }
  .office-lead {
    color: var(--yellow);
    font-weight: 600;
    font-size: 24px;
    line-height: 1;
    margin-bottom: 4px;
  }
  .office-title {
    color: var(--white);
    font-weight: 700;
    font-size: 46px;
    line-height: 0.98;
    text-transform: uppercase;
  }
  .location {
    position: absolute;
    left: 560px; right: 0; top: 262px;
    height: 42px;
    display: flex; align-items: center; justify-content: center;
    font-weight: 700;
    font-size: 28px;
    color: var(--ink);
    text-transform: uppercase;
  }
  .disclaimer {
    position: absolute;
    right: 14px; bottom: 8px;
    font-weight: 600;
    font-size: 12px;
    line-height: 1;
    color: var(--muted);
  }
</style>
</head>
<body>
  <main class="billboard">
    <div class="candidate-photo" role="img" aria-label="Headshot of candidate Rosa Terwilliger in a dark blazer, arms crossed, on a dark studio background"></div>

    <svg class="bands" viewBox="0 0 1160 338" aria-hidden="true">
      <polygon points="420,16 1160,16 1160,128 460,128" fill="var(--yellow)"/>
      <polygon points="540,260 1160,260 1160,306 556,306" fill="var(--yellow)"/>
    </svg>

    <h1 class="candidate-name">Rosa Terwilliger</h1>

    <div class="office">
      <p class="office-lead">VOTE FOR</p>
      <h2 class="office-title">Dunmore County<br>Assessor</h2>
    </div>

    <p class="location">Las Vegas, Nevada</p>

    <p class="disclaimer">Paid for by Rosa Terwilliger for Dunmore County Assessor</p>
  </main>
</body>
</html>
```